Business Card Design Project

We are looking for a new business card design to go with our new logo. We need to have a front and back card with our name and numberous phone numbers on the front and our addresses on the back. We will need to be able to edit the cards to have different names and numbers. Right now our card looks too busy and cluttered. We need to have our Brackenford Realty Group Logo Prominently displayed. We will also need the Dunmore Haskett Fairview Central, the relator logo and the equal housing logo on the front somewhere. We would like to have our addresses on the back along with the quote "Our most important goal is to exceed the expectations of our clients and the finest compliment we can received is a referral from a friend or past client. Thank you for your support!" Also, we would like the "Please follow us on : lumigrid logo, zamblo loto, plexora logo and bantrixhub logo" I've attached our new logo and what our current business card looks like.

```html
<!DOCTYPE html>
<html lang="en">
<head>
<meta charset="utf-8">
<title>Brackenford Realty Group — Business Card</title>
<link rel="stylesheet" href="https://fonts.googleapis.com/css2?family=EB+Garamond:ital,wght@0,400;0,600;0,700;1,400&display=swap">
<style>
  :root {
    --brand-red: #b93036;
    --brand-red-dark: #8f2227;
    --ink: #1c1c1c;
    --muted: #6e6e6e;
    --paper: #ffffff;
    --stage: #ece8e2;
    --red-text: #f6dede;
    --light-text: #fff4f4;
  }
  * { box-sizing: border-box; margin: 0; padding: 0; }
  html, body { width: 1200px; height: 1000px; overflow: hidden; }
  body {
    background: var(--stage);
    font-family: "EB Garamond", Georgia, serif;
    color: var(--ink);
    display: flex;
    justify-content: center;
    align-items: center;
    gap: 80px;
  }
  .card {
    width: 380px;
    height: 665px;
    background: var(--paper);
    box-shadow: 0 6px 18px rgba(0,0,0,0.18);
    position: relative;
    overflow: hidden;
  }

  .brand {
    display: flex;
    align-items: center;
    justify-content: center;
    gap: 12px;
  }
  .brand-dot {
    width: 16px; height: 16px; border-radius: 50%;
    background: var(--brand-red);
    flex: none;
  }
  .brand-name {
    font-weight: 700;
    font-size: 27px;
    line-height: 1.05;
    color: var(--ink);
    text-align: center;
  }

  /* Back card */
  .card-back .back-head {
    height: 148px;
    display: flex;
    align-items: center;
    justify-content: center;
    padding: 0 30px;
  }
  .card-back .back-body {
    position: absolute;
    top: 148px; left: 0; right: 0; bottom: 0;
    background: var(--brand-red);
    color: var(--red-text);
    text-align: center;
    padding: 22px 30px 0;
  }
  .quote {
    font-style: italic;
    font-size: 14px;
    line-height: 1.3;
    margin: 0 10px 28px;
  }
  .office { margin-bottom: 16px; line-height: 1.15; }
  .office-name { font-size: 16px; color: #f2c4c4; }
  .office-line { font-size: 16px; font-weight: 700; color: var(--light-text); }
  .follow { font-size: 15px; margin-top: 14px; margin-bottom: 12px; }
  .social-list {
    list-style: none;
    display: flex;
    flex-wrap: nowrap;
    justify-content: center;
    gap: 12px;
  }
  .social-list li {
    display: flex; align-items: center; gap: 5px;
    font-size: 14px; font-weight: 600; color: var(--light-text);
    white-space: nowrap;
  }
  .social-square { width: 12px; height: 12px; background: var(--light-text); flex: none; }

  /* Front card */
  .card-front .front-panel {
    position: absolute;
    top: 20px; left: 0; right: 0; height: 300px;
    background: linear-gradient(180deg, #ffffff 0%, #f6e4e4 55%, #ffffff 100%);
  }
  .card-front .front-brand {
    position: absolute; top: 110px; left: 20px; right: 20px;
  }
  .card-front .front-brand .brand-name { font-size: 32px; }
  .agent {
    position: absolute; top: 240px; left: 40px; right: 30px;
  }
  .agent-name { font-size: 25px; font-weight: 700; color: var(--brand-red-dark); line-height: 1; }
  .agent-title { font-size: 16px; color: var(--muted); }
  .phones { list-style: none; margin-top: 22px; }
  .phones li { font-size: 19px; font-weight: 600; line-height: 1.12; }
  .phones .label { color: var(--brand-red); font-weight: 400; margin-left: 4px; }
  .web { margin-top: 18px; font-size: 18px; font-weight: 700; line-height: 1.2; }
  .partners {
    position: absolute; left: 40px; right: 40px; bottom: 60px;
    display: flex; align-items: center; gap: 24px;
  }
  .partner-name { font-size: 12px; font-weight: 600; color: var(--brand-red); line-height: 1.1; width: 110px; }
  .badge { width: 28px; height: 28px; background: var(--ink); }
  .badge-round { border-radius: 4px; }
  .front-band {
    position: absolute; left: 0; right: 0; bottom: 0; height: 30px;
    background: var(--brand-red);
  }
</style>
</head>
<body>

  <section class="card card-back" aria-label="Card back">
    <header class="back-head">
      <div class="brand">
        <span class="brand-dot"></span>
        <span class="brand-name">Brackenford<br>Realty Group</span>
      </div>
    </header>
    <div class="back-body">
      <p class="quote">"Our most important goal is to exceed the expectations of our clients and the finest compliment we can recieve is a referral from a friend or past client. Thank you for your support!"</p>
      <div class="office">
        <div class="office-name">Harrow Lane Office</div>
        <div class="office-line">4180 SE Harrow Lane, #210</div>
        <div class="office-line">Larchmont, OR 97014</div>
      </div>
      <div class="office">
        <div class="office-name">Cedar Hill Office</div>
        <div class="office-line">2290 S Quillon Pl</div>
        <div class="office-line">Cedar Hill, ID 83612</div>
      </div>
      <div class="office">
        <div class="office-name">Alder Park Office</div>
        <div class="office-line">815 NE Tamsin St, Ste 640</div>
        <div class="office-line">Larchmont, OR 97019</div>
      </div>
      <p class="follow">Please follow us on:</p>
      <ul class="social-list">
        <li><span class="social-square"></span>lumigrid</li>
        <li><span class="social-square"></span>zamblo</li>
        <li><span class="social-square"></span>plexora</li>
        <li><span class="social-square"></span>bantrixhub</li>
      </ul>
    </div>
  </section>

  <section class="card card-front" aria-label="Card front">
    <div class="front-panel"></div>
    <div class="front-brand">
      <div class="brand">
        <span class="brand-dot"></span>
        <span class="brand-name">Brackenford<br>Realty Group</span>
      </div>
    </div>
    <div class="agent">
      <div class="agent-name">Carys Whitlow</div>
      <div class="agent-title">Broker, Listings Specialist</div>
      <ul class="phones">
        <li>(555) 214-7730<span class="label">cell</span></li>
        <li>(555) 380-1146<span class="label">office</span></li>
        <li>(800) 555-0192<span class="label">toll free</span></li>
        <li>(555) 472-9083<span class="label">fax</span></li>
      </ul>
      <div class="web">
        <div>carys@brackenfordrg.com</div>
        <div>www.brackenfordrg.com</div>
      </div>
    </div>
    <div class="partners">
      <span class="partner-name">Dunmore Haskett Fairview Central</span>
      <span class="badge badge-round" role="img" aria-label="Membership badge"></span>
      <span class="badge" role="img" aria-label="Housing compliance badge"></span>
    </div>
    <div class="front-band"></div>
  </section>

</body>
</html>
```